YouTube video thumbnail for my simple healthy recipes channel

Hi,

I need a thumbnail that I can re-use for all my videos and only substitute the photo of the recipe/food and maybe the name of the food/recipe if you will include that.

The goal is to attract young people (especially women) that are interested in simple healthy recipes. Please try to use light colors and preferably a shade of #a8d9de and or #debc63 to match my upcoming website.

Here is a Google Drive folder with some materials (photos etc.) to use. There is also a design of my new website so you can match the style.

https://filebox.examplestore.net/shared/7Qx2LmVpR8sTzKw3NbHd5yEa91?view=open

Here is my channel: https://www.vidplaza.example.org/c/VPmRt8ZqWnE2bLsHx7Yd4kGf

Thank you,
+Marta

Target Market(s)

Young Women

Industry/Entity Type

Nutritionist

Font styles to use
Other font styles liked:
• Lato preferred but you can be creative

Colors
ffffff

Requirements
Must have
• as above
Nice to have
• as above
Should not have
• as above

```html
<!DOCTYPE html>
<html lang="en">
<head>
<meta charset="utf-8">
<title>Recipe Thumbnails – Marta Kovell</title>
<link href="https://fonts.googleapis.com/css2?family=Lato:wght@400;700;900&display=swap" rel="stylesheet">
<style>
  :root {
    --canvas-bg: #7a7a7a;
    --band-gold: rgba(214, 178, 82, 0.88);
    --band-gold-solid: #d6b252;
    --title-white: #ffffff;
    --name-dark: #1e1e1e;
    --name-light: #ffffff;
    --title-shadow: rgba(60, 40, 10, 0.55);
  }
  * { margin: 0; padding: 0; box-sizing: border-box; }
  html, body {
    width: 695px; height: 1200px; overflow: hidden;
    background: var(--canvas-bg);
  }
  .canvas { position: relative; width: 695px; height: 1200px; }

  .thumbnail {
    position: absolute; left: 71px; width: 540px; height: 304px; overflow: hidden;
    font-family: "Lato", sans-serif;
  }
  .thumbnail--salmon { top: 79px; }
  .thumbnail--potatoes { top: 440px; width: 532px; }
  .thumbnail--salad { top: 816px; }

  .food-photo { position: absolute; inset: 0; }
  .thumbnail--salmon .food-photo {
    background:
      radial-gradient(ellipse 60% 75% at 72% 55%, #b5703a 0%, #a4612f 35%, #c89466 65%, rgba(230,224,226,0) 85%),
      linear-gradient(90deg, #d9d9d9 0%, #ebe8ea 40%, #efe8ec 100%);
  }
  .thumbnail--potatoes .food-photo {
    background:
      radial-gradient(ellipse 58% 85% at 75% 55%, #d6a94f 0%, #9a7a3c 40%, #6f7d3a 62%, rgba(255,255,255,0) 82%),
      linear-gradient(90deg, #ffffff 0%, #fbfbfb 45%, #f4f0e6 100%);
  }
  .thumbnail--salad .food-photo {
    background:
      radial-gradient(ellipse 40% 35% at 45% 75%, #d2412a 0%, rgba(210,65,42,0) 100%),
      radial-gradient(ellipse 45% 45% at 75% 40%, #5e9b2c 0%, rgba(94,155,44,0) 100%),
      radial-gradient(ellipse 80% 90% at 60% 60%, #4f8a28 0%, #2f3a24 70%, #3a3a3a 100%),
      linear-gradient(180deg, #f3f3f3 0%, #3c3c3c 25%);
  }

  .title-band {
    position: absolute; left: 0; height: 120px; width: 370px;
    background: var(--band-gold);
    display: flex; flex-direction: column; justify-content: center;
    padding-left: 20px;
  }
  .thumbnail--salmon .title-band { top: 71px; }
  .thumbnail--potatoes .title-band { top: 75px; width: 360px; padding-left: 13px; }
  .thumbnail--salad .title-band {
    top: 77px; width: 420px; padding-left: 37px;
    background: linear-gradient(90deg, var(--band-gold) 0%, var(--band-gold) 70%, rgba(214,178,82,0.5) 100%);
  }

  .recipe-title {
    color: var(--title-white);
    font-weight: 700;
    font-size: 33px;
    line-height: 40px;
    letter-spacing: 0.3px;
    text-transform: uppercase;
    text-shadow: 1px 2px 2px var(--title-shadow);
  }
  .recipe-kicker {
    color: var(--title-white);
    font-weight: 700; font-size: 17px; line-height: 20px;
    text-transform: uppercase; margin-bottom: 4px;
    text-shadow: 1px 1px 2px var(--title-shadow);
  }

  .channel-name {
    position: absolute; left: 22px;
    font-weight: 400; font-size: 30px;
    color: var(--name-dark);
  }
  .thumbnail--salmon .channel-name { top: 222px; }
  .thumbnail--potatoes .channel-name { top: 227px; left: 15px; }
  .thumbnail--salad .channel-name { top: 230px; left: 24px; color: var(--name-light); }
</style>
</head>
<body>
<main class="canvas">

  <section class="thumbnail thumbnail--salmon">
    <div class="food-photo" role="img" aria-label="Photo of golden fried vegetable salmon patties on a white plate"></div>
    <div class="title-band">
      <h2 class="recipe-title">Vegetable Packed<br>Salmon Patties</h2>
    </div>
    <p class="channel-name">Marta Kovell</p>
  </section>

  <section class="thumbnail thumbnail--potatoes">
    <div class="food-photo" role="img" aria-label="Photo of baked baby potatoes with mushrooms and fresh dill"></div>
    <div class="title-band">
      <h2 class="recipe-title">Baked Potatoes<br>With Mushrooms</h2>
    </div>
    <p class="channel-name">Marta Kovell</p>
  </section>

  <section class="thumbnail thumbnail--salad">
    <div class="food-photo" role="img" aria-label="Photo of a fresh salad with tomatoes, green onion, pickles and dill in a dark bowl"></div>
    <div class="title-band">
      <p class="recipe-kicker">5 Minute</p>
      <h2 class="recipe-title">Fresh Salad</h2>
    </div>
    <p class="channel-name">Marta Kovell</p>
  </section>

</main>
</body>
</html>
```